Website for Velmorund Capital, my new firm that raises money from investors to buy, build, own an...

Velmorund Capital needs a website! We are a new company with very experienced people, who invest in, own and build hotel properties, as well as apartments and other commercial real estate. We seek investors for our projects, and we provide safe, secure returns on their investment in our projects. Our new logo is designed to exhibit strength, class and security, and would like our website to continue on this theme. Our name, Velmorund, is a word-play on a Greek word “aristeia”, which means “excellence” and “a warriors finest moment of glory in war”. If you are in business, you realize that much of it is like war, with strategy and moves and opponents and competitors, and ever-changing economic conditions and threats that make business very much like war. We like to think that we are good at business (war), and so have named our company “Velmorund”, using the founders last name and the word “aristeia” combined. Another definition of "aristeia" is "performing at the peak of one's potential after a long struggle"...again, much like business in real life! The website design should exhibit financial security, smart moves, and positive growth towards a bright future.

Target Market(s)

The target market is smart and wealthy investors, with others such as brokers, cities and government agencies, lenders, sellers, partners, etc also looking at it.

Industry/Entity Type

Investment

Number of Pages Required

5+ page

Font styles to use
Sans Serif

Colors
fec214

Requirements
Must have
• Our website should have a landing page, a "about" or bio page, a projects page and a contact us page. Our new logo uses the colors black and gold, so this should be factored in to our site. The site should be simple, yet impactful and impressive. I have actually two logos, which can be mixed and interchanged in a complimentary way, each with their own unique look.
Nice to have
• I have uploaded a couple screenshots of a website i like, and the simplicity I mention.
Should not have
• The site should not be flashy or complicated or complex or "busy"

```html
<!DOCTYPE html>
<html lang="en">
<head>
<meta charset="utf-8">
<title>Velmorund Capital</title>
<link rel="stylesheet" href="https://fonts.googleapis.com/css2?family=Montserrat:wght@400;500;600;700&display=swap">
<style>
  :root {
    --gold: #fec214;
    --ink: #111111;
    --dark: #1d1d1d;
    --white: #ffffff;
    --muted: #8a8a8a;
  }
  * { margin: 0; padding: 0; box-sizing: border-box; }
  html, body { width: 1200px; height: 1200px; overflow: hidden; background: var(--white); }
  body { font-family: "Montserrat", sans-serif; color: var(--ink); }
  .page {
    position: absolute; left: 327px; top: 0;
    width: 681px; height: 1500px;
    transform: scale(0.8); transform-origin: 0 0;
    background: var(--white); overflow: hidden;
  }
  .abs { position: absolute; }

  /* hero */
  .hero-art { position: absolute; left: 0; top: 0; }
  .brand { left: 74px; top: 24px; display: flex; align-items: center; gap: 6px; }
  .brand-mark { width: 14px; height: 14px; background: var(--gold); }
  .brand-name { font-size: 10px; font-weight: 700; color: var(--white); letter-spacing: .5px; }
  .nav { left: 225px; top: 40px; display: flex; gap: 19px; font-size: 14px; font-weight: 600; color: var(--white); }
  .nav .active { color: var(--gold); }
  .hero-title { left: 73px; top: 122px; font-size: 21px; font-weight: 700; line-height: 25px; color: var(--white); }
  .hero-text { left: 74px; top: 181px; font-size: 13.5px; line-height: 16px; color: var(--white); width: 360px; }
  .btn { display: flex; align-items: center; justify-content: center; font-size: 10px; font-weight: 700; color: var(--white); }
  .btn-fill { left: 74px; top: 239px; width: 78px; height: 32px; background: var(--gold); }
  .btn-line { left: 166px; top: 239px; width: 78px; height: 32px; border: 2px solid var(--gold); }

  /* cards */
  .card { top: 378px; height: 136px; background: var(--gold); padding: 25px 33px; }
  .card h3 { font-size: 13.5px; font-weight: 700; margin-bottom: 3px; }
  .card p { font-size: 11.5px; line-height: 13.5px; }
  .card .more { position: absolute; bottom: 17px; font-size: 11.5px; }
  .card-about { left: 74px; width: 248px; }
  .card-mission { left: 357px; width: 250px; padding-left: 42px; }

  /* section heads */
  .section-head { left: 0; width: 681px; text-align: center; font-size: 17px; font-weight: 500; }
  .rule { left: 314px; width: 53px; height: 3px; background: var(--gold); }
  .services-text { left: 110px; top: 604px; width: 462px; text-align: center; font-size: 11.5px; line-height: 13.7px; }
  .services-text .link { color: var(--gold); }

  /* reasons */
  .reason { top: 762px; }
  .reason h4 { font-size: 11.5px; font-weight: 500; margin-bottom: 4px; }
  .reason p { font-size: 7.6px; line-height: 10px; }

  /* stats */
  .stats { left: 0; top: 874px; width: 681px; height: 107px; background: linear-gradient(90deg, #f3c22a 0%, #e9bb2e 45%, #e4b62e 100%); }
  .stat { top: 884px; color: var(--white); }
  .stat b { display: block; font-size: 40px; font-weight: 700; line-height: 48px; }
  .stat span { font-size: 13.5px; color: #fff4cc; }

  /* testimonial */
  .portrait { left: 74px; top: 1070px; width: 124px; height: 148px; background: linear-gradient(160deg, #ddd6cd, #a98f7c 55%, #3f5a44); }
  .quote-text { left: 254px; top: 1068px; width: 312px; font-size: 11.5px; line-height: 13.7px; }
  .quote-name { left: 256px; top: 1150px; font-size: 11.5px; line-height: 14px; }
  .quote-name b { font-weight: 700; }
  .dots { left: 255px; top: 1207px; display: flex; gap: 1px; }
  .dots i { width: 10px; height: 10px; border-radius: 50%; border: 1px solid var(--muted); }
  .dots i:first-child { border-color: var(--gold); }

  /* footer */
  .footer { left: 0; top: 1264px; width: 681px; height: 236px; background: var(--dark); color: var(--white); }
  .foot-head { top: 1286px; font-size: 13.5px; font-weight: 500; }
  .foot-text { font-size: 10.5px; line-height: 12px; color: var(--white); }
  .field-label { font-size: 7.5px; color: var(--white); }
  .field-line { left: 300px; width: 171px; height: 3px; background: var(--gold); }
  .submit { left: 300px; top: 1409px; width: 57px; height: 23px; border: 2px solid var(--gold); font-size: 7.5px; display: flex; align-items: center; justify-content: center; color: var(--white); }
  .social { left: 530px; display: flex; align-items: center; gap: 9px; font-size: 10.5px; }
  .social i { width: 27px; height: 27px; border-radius: 50%; background: #3d5a98; }
  .copy { left: 0; width: 681px; top: 1468px; text-align: center; font-size: 10px; color: var(--white); }
</style>
</head>
<body>
<div class="page">

  <svg class="hero-art" width="681" height="360" viewBox="0 0 681 360" role="img" aria-label="Photo of a modern multi-storey hotel building at dusk with a landscaped forecourt">
    <defs>
      <linearGradient id="sky" x1="0" y1="0" x2="0" y2="1">
        <stop offset="0" stop-color="#3b4c66"/>
        <stop offset="0.55" stop-color="#7d8594"/>
        <stop offset="0.8" stop-color="#4c5348"/>
        <stop offset="1" stop-color="#1e1f22"/>
      </linearGradient>
    </defs>
    <path d="M0 0 H681 V285 Q340 430 0 288 Z" fill="url(#sky)"/>
  </svg>

  <div class="abs brand"><span class="brand-mark"></span><span class="brand-name">VELMORUND</span></div>
  <nav class="abs nav">
    <span class="active">Home</span><span>About Us</span><span>Services</span><span>Projects</span><span>Contact Us</span>
  </nav>
  <h1 class="abs hero-title">Discover the world<br>of secure investments</h1>
  <p class="abs hero-text">Experiencefinancial security, Positive growth - all of which is reflected in the quality of our results</p>
  <a class="abs btn btn-fill">Read More</a>
  <a class="abs btn btn-line">Contact Us</a>

  <div class="abs card card-about">
    <h3>About Company</h3>
    <p>A company with experienced<br>experts helping investors find<br>the best return on investments.</p>
    <span class="more">Read More</span>
  </div>
  <div class="abs card card-mission">
    <h3>Our Misssion</h3>
    <p>Reducing risk and making<br>smart moves toward a bright<br>future.</p>
    <span class="more">Read More</span>
  </div>

  <h2 class="abs section-head" style="top:556px">Our Services</h2>
  <div class="abs rule" style="top:580px"></div>
  <p class="abs services-text">We are an experienced company which invests in, own and build properties ranging from hotel properties, Apartments and other commercial real estate. We help investors get safe and secure returns on their investments in our projects. <span class="link">Read More</span></p>

  <h2 class="abs section-head" style="top:710px">Why Choose Us</h2>
  <div class="abs rule" style="top:737px"></div>

  <svg class="abs" style="left:74px;top:764px" width="26" height="36" viewBox="0 0 26 36">
    <rect x="1" y="4" width="22" height="14" rx="2" fill="#fec214"/>
    <rect x="8" y="1" width="8" height="4" fill="none" stroke="#fec214" stroke-width="2"/>
    <circle cx="14" cy="25" r="8" fill="#fff" stroke="#111" stroke-width="2.5"/>
    <path d="M14 20 V25 H17" stroke="#111" stroke-width="2" fill="none"/>
  </svg>
  <div class="abs reason" style="left:104px;width:140px">
    <h4>Operational Excellence</h4>
    <p>Company provide outstanding service through teamwork, ac-countability and innovation of which is reflected.</p>
  </div>

  <svg class="abs" style="left:251px;top:764px" width="26" height="24" viewBox="0 0 26 24">
    <rect x="2" y="4" width="18" height="18" fill="none" stroke="#fec214" stroke-width="2.5"/>
    <path d="M6 12 L11 17 L24 3" stroke="#fec214" stroke-width="3" fill="none"/>
  </svg>
  <div class="abs reason" style="left:289px;width:140px">
    <h4>Financial Security</h4>
    <p>Our investors can be rest as-sured that we can provide them safe and secure returns on their investments.</p>
  </div>

  <svg class="abs" style="left:438px;top:764px" width="24" height="24" viewBox="0 0 24 24">
    <circle cx="12" cy="12" r="10" fill="none" stroke="#fec214" stroke-width="2"/>
    <circle cx="12" cy="12" r="6" fill="none" stroke="#fec214" stroke-width="2"/>
    <circle cx="12" cy="12" r="2.5" fill="#fec214"/>
  </svg>
  <div class="abs reason" style="left:474px;width:140px">
    <h4>Growth</h4>
    <p>We are warriors because of that we hit the bullseye everytime causing positive growth while exhibiting strength and class.</p>
  </div>

  <div class="abs stats" role="img" aria-label="Yellow-tinted photo of apartment buildings behind the company figures"></div>
  <div class="abs stat" style="left:73px"><b>1267</b><span>Satisfied Clients</span></div>
  <div class="abs stat" style="left:301px"><b>450</b><span>Finished Projects</span></div>
  <div class="abs stat" style="left:527px"><b>350</b><span>Employees</span></div>

  <h2 class="abs section-head" style="top:1020px">What People are Saying</h2>
  <div class="abs rule" style="top:1046px"></div>
  <div class="abs portrait" role="img" aria-label="Portrait photo of the client giving the testimonial"></div>
  <svg class="abs" style="left:212px;top:1070px" width="32" height="26" viewBox="0 0 32 26">
    <path d="M2 2 H13 V13 Q13 22 4 25 L3 21 Q8 19 8 14 H2 Z M18 2 H29 V13 Q29 22 20 25 L19 21 Q24 19 24 14 H18 Z" fill="#fec214"/>
  </svg>
  <p class="abs quote-text">We have chosen to work extensively with Velmorund because of their quality services, and employer incen-tives that helped reduced our hiring cost. Attract and retail high quality customers.</p>
  <p class="abs quote-name"><b>- Elena Marsh</b><br>CTO at Brightwell Labs</p>
  <div class="abs dots"><i></i><i></i><i></i></div>

  <footer class="abs footer"></footer>
  <h3 class="abs foot-head" style="left:74px;color:#fff">SATELLITE OFFICE</h3>
  <p class="abs foot-text" style="left:73px;top:1322px">48 Harcourt Lane, N 7QR<br>London, UK</p>
  <p class="abs foot-text" style="left:73px;top:1359px">+1 555 - 0142 - 318</p>
  <p class="abs foot-text" style="left:76px;top:1383px">head@velmorund.com</p>

  <h3 class="abs foot-head" style="left:300px;color:#fff">REQUEST A CALL</h3>
  <span class="abs field-label" style="left:301px;top:1322px">NAME</span>
  <div class="abs field-line" style="top:1334px"></div>
  <span class="abs field-label" style="left:301px;top:1347px">EMAIL</span>
  <div class="abs field-line" style="top:1359px"></div>
  <span class="abs field-label" style="left:301px;top:1373px">MESSAGE</span>
  <div class="abs field-line" style="top:1384px"></div>
  <div class="abs submit">SUMMIT</div>

  <h3 class="abs foot-head" style="left:527px;color:#fff">FOLLOW</h3>
  <div class="abs social" style="top:1320px;color:#fff"><i></i>Friendloop</div>
  <div class="abs social" style="top:1361px;color:#fff"><i></i>Workline</div>
  <div class="abs social" style="top:1408px;color:#fff"><i></i>Snapframe</div>

  <p class="abs copy">CopRight 2018 All Rights Reserved</p>
</div>
</body>
</html>
```